Interior Design/ decoration business card design

This card is for my Interior Design and Decoration business and later I will also be selling homewares. I would like the card to be very simple in design and like either white, duck egg blue , aquas or metallics on a flat mat card excellent quality card. It needs to be well designed as that is my field. I dont like fuss, the simpler the better. I would like a styalised wren under the name wren if possible. SIMPLE, STYLISH, CLASSIC, TASTEFUL

Target Market(s)

40 + year olds who are building or rennovating.

Industry/Entity Type

Business

Contact Information for Business Card

Wren
styling, design, homeware

Marnie Tolland
p 0427316958
e marnie@wrenliving.com.au
w wrenliving.com.au

Requirements
Must have
• very simple, stylish, classic, sophisticated. Simple and easy to read text that is a print similar to attached image. I like simple round A's though not as in attached image.

Double sided. It wont save as double sided for some reason!!
Should not have
• not too much colour, No animated / cartoon pictures.

```html
<!DOCTYPE html>
<html lang="en">
<head>
<meta charset="utf-8">
<title>Wren — Business Card, Front and Back</title>
<link href="https://fonts.googleapis.com/css2?family=Arimo:wght@400;700&display=swap" rel="stylesheet">
<style>
  :root {
    --stage: #d9d9d9;
    --paper: #ffffff;
    --duck-egg: #bcd9d6;
    --ink: #1e1e1e;
    --accent-red: #d71920;
  }
  * { margin: 0; padding: 0; box-sizing: border-box; }
  html, body {
    width: 1200px;
    height: 960px;
    overflow: hidden;
  }
  body {
    background: var(--stage);
    font-family: "Arimo", Arial, sans-serif;
    color: var(--ink);
    position: relative;
  }
  .card {
    position: absolute;
    width: 690px;
    height: 418px;
  }
  .card--front {
    left: 108px;
    top: 48px;
    background: var(--paper);
  }
  .card--back {
    left: 402px;
    top: 494px;
    background: var(--duck-egg);
  }

  .wordmark {
    position: absolute;
    font-weight: 400;
    color: var(--ink);
    letter-spacing: 0.14em;
    line-height: 1;
  }
  .card--front .wordmark {
    left: 0;
    right: 0;
    top: 130px;
    text-align: center;
    font-size: 64px;
  }
  .card--back .wordmark {
    left: 420px;
    width: 200px;
    top: 92px;
    text-align: center;
    font-size: 46px;
  }

  .services {
    position: absolute;
    left: 0;
    right: 0;
    top: 344px;
    display: flex;
    justify-content: center;
    align-items: center;
    font-size: 17px;
  }
  .services__item { padding: 0 14px; }
  .services__divider {
    width: 2px;
    height: 24px;
    background: var(--accent-red);
  }

  .holder {
    position: absolute;
    left: 38px;
    top: 100px;
    font-size: 18px;
    font-variant: small-caps;
    font-weight: 700;
    letter-spacing: 0.02em;
  }
  .holder__surname { color: var(--accent-red); }

  .contacts {
    position: absolute;
    left: 38px;
    top: 176px;
    list-style: none;
    font-size: 16px;
  }
  .contacts__line {
    display: flex;
    align-items: center;
    gap: 8px;
    height: 24px;
  }
  .contacts__icon {
    width: 18px;
    height: 16px;
    flex: none;
  }
</style>
</head>
<body>

  <section class="card card--front" aria-label="Card front">
    <p class="wordmark">wren</p>
    <p class="services">
      <span class="services__item">Decoration</span>
      <span class="services__divider"></span>
      <span class="services__item">styling</span>
      <span class="services__divider"></span>
      <span class="services__item">Homeware</span>
    </p>
  </section>

  <section class="card card--back" aria-label="Card back">
    <p class="holder">Marnie <span class="holder__surname">Tolland</span></p>

    <ul class="contacts">
      <li class="contacts__line">
        <svg class="contacts__icon" viewBox="0 0 18 16" aria-hidden="true">
          <path d="M1 5 Q9 0 17 5 L15 7 L12 5.5 L12 4 Q9 3 6 4 L6 5.5 L3 7 Z" fill="#1e1e1e"/>
          <rect x="3" y="8" width="12" height="7" rx="1" fill="#1e1e1e"/>
          <circle cx="9" cy="11.5" r="2" fill="#bcd9d6"/>
        </svg>
        <span>0427316958</span>
      </li>
      <li class="contacts__line">
        <svg class="contacts__icon" viewBox="0 0 18 16" aria-hidden="true">
          <rect x="1" y="3" width="16" height="11" fill="#1e1e1e"/>
          <path d="M1.5 3.5 L9 9.5 L16.5 3.5" fill="none" stroke="#bcd9d6" stroke-width="1.3"/>
        </svg>
        <span>marnie@wrenliving.com.au</span>
      </li>
      <li class="contacts__line">
        <svg class="contacts__icon" viewBox="0 0 18 16" aria-hidden="true">
          <g fill="none" stroke="#1e1e1e" stroke-width="1.2">
            <circle cx="9" cy="8" r="7"/>
            <ellipse cx="9" cy="8" rx="3" ry="7"/>
            <line x1="2" y1="8" x2="16" y2="8"/>
            <path d="M3.2 4.5 H14.8 M3.2 11.5 H14.8"/>
          </g>
        </svg>
        <span>wrenliving.com.au</span>
      </li>
    </ul>

    <p class="wordmark">wren</p>
  </section>

</body>
</html>
```